Wellness bold & beautiful PowerPoint Template

I will like a PowerPoint template, matching my brand, designed for my business.
- Some words that describe our brand identity are: wellness, natural, calming, simplicity, clean
- For icons, we prefer line icons.
- Website: http://www.verinaxo.com/
- PowerPoint board: https://www.pinboardly.com/tesmaruli/verinaxo-powerpoint/
- Branding board: https://www.pinboardly.com/tesmaruli/verinaxo-branding/
FYI: I am attaching a rough draft of a powerpoint presentation we are preparing
Target Market(s)
Women 23-48 interested in wellness
Industry/Entity Type
Health And Wellness
Font styles to use
Other font styles liked:
- Open Sans, Helvitica, Meddon
Requirements
Must have
- cover page, about page, author page, table of content, table format, graph format, list format, 2 column template.
Nice to have
- time line page sample

```html
<!DOCTYPE html>
<html lang="en">
<head>
<meta charset="utf-8">
<title>Verinaxo – Unclutter Your Space template</title>
<link href="https://fonts.googleapis.com/css2?family=Smokum&family=Open+Sans:wght@400;600;700&display=swap" rel="stylesheet">
<style>
  :root{
    --board:#6b6b6b;
    --paper:#ffffff;
    --ink:#1d1d1d;
    --magenta:#a4307f;
    --magenta-dark:#7a2360;
    --teal:#1e9b86;
    --teal-dark:#15776a;
    --green:#3fae6a;
    --lime-a:#d3ec8c;
    --lime-b:#79bb3a;
    --mint:#dff1ec;
    --bullet:#e0607a;
    --head:'Smokum', serif;
    --body:'Open Sans', Arial, sans-serif;
  }
  *{box-sizing:border-box;margin:0;padding:0}
  html,body{width:1200px;height:775px;overflow:hidden;background:var(--board)}
  .board{position:relative;width:1200px;height:775px}
  .slide{position:absolute;width:378px;height:210px;background:var(--paper);overflow:hidden;font-family:var(--body);color:var(--ink)}
  .c1{left:16px}.c2{left:412px}.c3{left:808px}
  .r1{top:37px}.r2{top:275px}.r3{top:521px}
  .footer{position:absolute;left:0;right:0;bottom:0;height:12px;background:linear-gradient(180deg,var(--lime-a),var(--lime-b));font-size:5px;color:#fff;display:flex;justify-content:space-between;align-items:center;padding:0 22px 0 36px}
  .title{position:absolute;left:30px;top:14px;font-family:var(--head);font-weight:400;font-size:14px;letter-spacing:.6px;color:var(--ink)}
  .bullets{position:absolute;left:30px;top:47px;list-style:none;font-size:7.5px;line-height:18.6px}
  .bullets li::before{content:"»";color:var(--bullet);margin-right:8px}
  /* cover */
  .cover-photo{position:absolute;inset:0;background:linear-gradient(120deg,#2fb79a 0%,#8fd2a8 35%,#f3e7a4 65%,#f7c56a 100%)}
  .brand{position:absolute;left:40px;top:42px;display:flex;align-items:center;gap:5px;font-weight:700;font-size:11px;color:var(--magenta)}
  .brand .dot{width:12px;height:12px;border-radius:50%;background:var(--teal)}
  .cover-title{position:absolute;left:30px;top:94px;font-family:var(--head);font-weight:400;font-size:30px;line-height:32px;letter-spacing:1px;color:#222}
  .cover-by{position:absolute;left:32px;top:160px;font-size:5.5px;line-height:9px;color:#222;font-weight:600}
  .cover-url{position:absolute;left:32px;bottom:7px;font-size:5px;color:#fff}
  /* thanks */
  .seal{position:absolute;left:136px;top:18px;width:100px;height:100px;border-radius:50%;background:var(--mint);display:flex;align-items:center;justify-content:center;font-weight:700;font-size:12px;color:var(--magenta)}
  .thanks{position:absolute;left:0;right:0;top:132px;text-align:center;font-family:var(--head);font-weight:400;font-size:22px;letter-spacing:.5px}
  /* about */
  .banner{position:absolute;left:0;right:0;top:45px;height:113px;background:linear-gradient(180deg,#3a1f6b 0%,#8a3f8f 45%,#e0708a 70%,#5b3a8a 100%);color:#fff;text-align:center}
  .banner .quote{position:absolute;left:0;width:300px;top:32px;font-family:var(--head);font-size:12px;letter-spacing:.4px}
  .banner .tag{position:absolute;left:45px;width:210px;top:54px;font-size:8px;line-height:13px}
  /* question */
  .faint{position:absolute;left:95px;top:12px;width:190px;height:180px;border-radius:50%;background:var(--mint);opacity:.7}
  .question{position:absolute;left:0;right:0;top:100px;text-align:center;font-family:var(--head);font-weight:400;font-size:16px;letter-spacing:.4px}
  /* agenda */
  .agenda{position:absolute;top:47px;list-style:none;font-size:6px;line-height:10.6px}
  .agenda.left{left:30px}.agenda.right{left:196px;width:150px}
  .agenda li::before{content:"»";color:var(--bullet);margin-right:6px}
  .agenda .sub{list-style:none;padding-left:10px}
  .agenda .sub li{line-height:10.6px;font-size:5.5px}
  .agenda.right .sub li{line-height:8px}
  .agenda .wrap{padding-left:11px;text-indent:-11px;line-height:8px;margin:1px 0 2px}
  .chart{position:absolute;left:0;top:0}
</style>
</head>
<body>
<main class="board">

  <section class="slide c1 r1">
    <div class="cover-photo" role="img" aria-label="Sunlit photo of a woman in a white dress with arms open"></div>
    <div class="brand"><span class="dot"></span>Verinaxo</div>
    <h1 class="cover-title">UNCLUTTER<br>YOUR SPACE</h1>
    <p class="cover-by">Tes Maruli @ Verinaxo<br>Ilka Dorren @ Simplifying with Ilka</p>
    <span class="cover-url">www.verinaxo.com</span>
  </section>

  <section class="slide c2 r1">
    <div class="seal">Verinaxo</div>
    <h2 class="thanks">THANKS FOR COMMING!!</h2>
    <div class="footer"><span>www.verinaxo.com</span><span>01</span></div>
  </section>

  <section class="slide c3 r1">
    <h2 class="title">INTRODUCTION - TES</h2>
    <ul class="bullets">
      <li>Software Engineer by Training</li>
      <li>Mom of 2 boys</li>
      <li>Since 2010, developing a holistic lifestyle</li>
      <li>Knack for organization and efficiency</li>
      <li>Creating a happier more balanced life for me and my family</li>
    </ul>
    <div class="footer"><span>www.verinaxo.com</span><span>02</span></div>
  </section>

  <section class="slide c1 r2">
    <h2 class="title">ABOUT VERINAXO</h2>
    <div class="banner" role="img" aria-label="Sunset beach photo with a cyclist silhouette">
      <p class="quote">“SUPPORTING YOUR WELLNESS JOURNEY”</p>
      <p class="tag">Helping people live healthier (happier) more balanced and holistic lives</p>
    </div>
    <div class="footer"><span>www.verinaxo.com</span><span>03</span></div>
  </section>

  <section class="slide c2 r2">
    <h2 class="title">INTRODUCTION - ILKA</h2>
    <ul class="bullets">
      <li>…</li>
      <li>Mom of 2 boys</li>
      <li>Since 2010, developing a blog for a simplified lifestyle</li>
      <li>Simplifying with Ilka</li>
    </ul>
    <div class="footer"><span>www.verinaxo.com</span><span>04</span></div>
  </section>

  <section class="slide c3 r2">
    <div class="faint"></div>
    <h2 class="question">WHAT BRINGS YOU HERE TODAY?</h2>
    <div class="footer"><span>www.verinaxo.com</span><span>05</span></div>
  </section>

  <section class="slide c1 r3">
    <h2 class="title">AGENDA</h2>
    <ul class="agenda left">
      <li>Why Unclutter</li>
      <li>The Point of Frustration</li>
      <li>Failed Attempts</li>
      <li>Getting Help</li>
      <li>Steps to creating your best space
        <ul class="sub"><li>Declutter</li><li>Organize</li><li>Rejuvenate</li><li>Maintain</li></ul>
      </li>
      <li>Before &amp; After</li>
      <li>Keeping it real!</li>
    </ul>
    <ul class="agenda right">
      <li>Getting Started</li>
      <li>Declutter Action Plan</li>
      <li class="wrap">Organizational principles – Tips &amp; Tricks</li>
      <li>Feng Shui 101</li>
      <li>It's not just the clutter</li>
      <li>Zero Waste Movement</li>
      <li>Getting stuck
        <ul class="sub"><li>Gatherly Forum</li><li>Professional help</li></ul>
      </li>
      <li>Resources</li>
    </ul>
    <div class="footer"><span>www.verinaxo.com</span><span>06</span></div>
  </section>

  <section class="slide c2 r3">
    <h2 class="title">EFFECTS OF UNCLUTTER</h2>
    <svg class="chart" width="378" height="210" viewBox="0 0 378 210" font-family="Open Sans, sans-serif">
      <polygon points="35,47 55,47 74,79 74,109 35,89" fill="var(--teal-dark)"/>
      <polygon points="35,93 74,105 74,135 35,131" fill="var(--magenta-dark)"/>
      <polygon points="35,136 74,136 74,164 55,175 35,175" fill="var(--teal-dark)"/>
      <rect x="2" y="47" width="33" height="42" fill="var(--green)"/>
      <rect x="2" y="93" width="33" height="38" fill="var(--magenta)"/>
      <rect x="2" y="136" width="33" height="39" fill="var(--green)"/>
      <g fill="#fff" font-size="10" text-anchor="middle"><text x="18" y="72">01</text><text x="18" y="116">02</text><text x="18" y="159">03</text></g>
      <polygon points="74,79 228,79 236,94 228,109 74,109" fill="var(--green)"/>
      <polygon points="74,106 214,106 222,120 214,135 74,135" fill="var(--magenta)"/>
      <polygon points="74,136 236,136 244,150 236,164 74,164" fill="var(--green)"/>
      <g fill="#fff" font-size="6.5" text-anchor="middle">
        <text x="150" y="96">What does a cluttered space do to you?</text>
        <text x="144" y="118">What does an uncluttered</text><text x="144" y="127">space do for you?</text>
        <text x="156" y="148">What does this do to other areas of your</text><text x="156" y="157">life?</text>
      </g>
    </svg>
    <div class="footer"><span>www.verinaxo.com</span><span>05</span></div>
  </section>

  <section class="slide c3 r3">
    <h2 class="title">EFFECTS OF UNCLUTTER</h2>
    <svg class="chart" width="378" height="210" viewBox="0 0 378 210" font-family="Open Sans, sans-serif">
      <polygon points="106,41 90,77 110,77" fill="#8a8a8a"/>
      <polygon points="106,41 110,77 122,73" fill="#5e5e5e"/>
      <polygon points="80,82 134,82 140,94 140,109 72,109 72,96" fill="var(--teal)"/>
      <polygon points="134,82 140,94 140,109 137,100" fill="var(--teal-dark)"/>
      <polygon points="64,112 148,112 157,126 157,144 54,144 54,128" fill="var(--magenta)"/>
      <polygon points="148,112 157,126 157,144 153,132" fill="var(--magenta-dark)"/>
      <polygon points="46,147 166,147 177,162 177,181 32,181 32,164" fill="var(--teal)"/>
      <polygon points="166,147 177,162 177,181 172,168" fill="var(--teal-dark)"/>
      <g fill="#fff" font-size="9" text-anchor="middle"><text x="106" y="100">01</text><text x="106" y="133">02</text><text x="106" y="169">03</text></g>
      <g fill="#1d1d1d" font-size="7.5">
        <text x="144" y="91">What does a cluttered space do to you?</text>
        <text x="158" y="121">What does an uncluttered space do for you?</text>
        <text x="178" y="150">What does this do to other areas of</text><text x="183" y="160">your life?</text>
      </g>
    </svg>
    <div class="footer"><span>www.verinaxo.com</span><span>06</span></div>
  </section>

</main>
</body>
</html>
```